Keystone Allies Website

My business has been word of mouth over the last 3 years and has grown. Now I need a website for additional marketing as we have new clients asking for a website.

You have already completed my Logo during an earlier project. I have attached the logo.

We do Staff Augmentation and Operation Support.

What is that?
Staff augmentation is an outsourcing strategy that allows companies to fill specific, temporary roles to achieve business objectives. This staffing method complements existing teams with specific talent, enhancing business capabilities or filling gaps left by members on extended leave.

We work alongside the internal recruiting team to assist clients to meet and exceed financial goals.

```html
<!DOCTYPE html>
<html lang="en">
<head>
<meta charset="utf-8">
<title>Keystone Allies</title>
<link href="https://fonts.googleapis.com/css2?family=Montserrat:wght@300;400;600;700;800&family=Roboto:wght@400;500;700&display=swap" rel="stylesheet">
<style>
:root{
  --navy:#0b4f7c;
  --navy-deep:#123a63;
  --blue:#1a6aa3;
  --ink:#333a42;
  --muted:#6b7078;
  --line:#d5dbe1;
  --white:#ffffff;
  --grey:#8c8f93;
  --pale:#e8eff4;
  --foot-bar:#e4ebf2;
}
*{box-sizing:border-box;margin:0;padding:0}
html,body{width:1200px;height:3791px;overflow:hidden}
body{font-family:"Roboto",sans-serif;color:var(--ink);background:var(--white);position:relative}
.abs{position:absolute}
.heading{font-family:"Montserrat",sans-serif;font-weight:300;letter-spacing:.5px}
.heading b{font-weight:800}

/* header */
.site-header{position:absolute;left:0;top:0;width:1200px;height:88px;background:var(--white);border-top:2px solid #9fd3e8}
.brand{position:absolute;left:88px;top:14px;display:flex;align-items:center;gap:10px}
.brand-dot{width:44px;height:44px;border-radius:50%;background:var(--navy)}
.brand-name{font-family:"Montserrat",sans-serif;font-weight:700;color:var(--navy);font-size:24px;line-height:1.05}
.main-nav{position:absolute;left:0;top:0;width:1200px;height:88px}
.main-nav .nav-link{position:absolute;top:0;height:86px;line-height:86px;font-family:"Roboto",sans-serif;font-size:14px;color:#7a8088;text-decoration:none;white-space:nowrap}
.main-nav .nav-link.active{color:var(--navy);font-weight:500}
.main-nav .nav-link.active::after{content:"";position:absolute;left:-7px;right:-7px;bottom:0;height:3px;background:var(--navy)}
.nav-cta{position:absolute;left:972px;top:24px;width:138px;height:42px;border:2px solid var(--navy);border-radius:22px;color:var(--navy);font-weight:700;font-size:13px;text-align:center;line-height:38px;white-space:nowrap}

/* buttons */
.btn-solid{position:absolute;background:var(--navy);color:#fff;border-radius:30px;font-family:"Roboto",sans-serif;font-weight:700;font-size:16px;display:flex;align-items:center;justify-content:center;padding-right:24px}
.btn-solid::after{content:"";position:absolute;right:8px;top:50%;width:24px;height:24px;margin-top:-12px;border-radius:50%;border:3px solid rgba(120,190,230,.55)}
.btn-ghost{position:absolute;border:2px solid #fff;border-radius:30px;color:#fff;font-weight:700;font-size:15px;text-align:center}

/* hero */
.hero{position:absolute;left:0;top:88px;width:1200px;height:620px;background:radial-gradient(circle at 75% 40%,#4fb4e8 0%,#1b6ea8 35%,#0d3b66 75%,#0a2c4f 100%)}
.hero-title{position:absolute;left:141px;top:180px;color:#fff;font-family:"Montserrat",sans-serif;font-size:36px;font-weight:300;line-height:1.25}
.hero-title b{font-weight:800;font-size:40px;display:block}
.hero-text{position:absolute;left:148px;top:285px;width:380px;color:#e6f0f8;font-size:15px;line-height:27px}
.arrow{position:absolute;top:260px}

/* about */
.about-media{position:absolute;left:140px;top:758px;width:346px;height:427px;border-radius:50%;background:radial-gradient(circle,#dbe6ef 0%,#8fa8c4 55%,#2f5a8a 100%)}
.kicker{font-family:"Montserrat",sans-serif;font-weight:400;font-size:20px;color:var(--muted);letter-spacing:.5px}
.sec-title{font-family:"Montserrat",sans-serif;font-weight:400;font-size:33px;color:var(--navy)}
.sec-title b{font-weight:800}
.underline{position:absolute;height:4px;width:52px;background:var(--navy)}
.para{font-size:15px;line-height:27px;color:var(--ink)}

/* services */
.service-label{position:absolute;text-align:center;color:#fff}
.service-label h3{font-family:"Montserrat",sans-serif;font-weight:300;font-size:30px;letter-spacing:.5px}
.service-label h3 b{font-weight:800}
.service-label .bar{width:46px;height:4px;background:#fff;margin:14px auto 18px}
.service-label p{font-size:14px;line-height:25px}

/* why */
.why{position:absolute;left:0;top:1811px;width:1200px;height:556px;background:linear-gradient(90deg,#3d4e60 0%,#8ea4b8 35%,#dbe6ee 55%,#e6eef4 100%)}

/* blog */
.post{position:absolute;top:2510px;width:303px;height:362px;border:1px solid var(--line);background:#fff}
.post-photo{width:100%;height:203px;background:linear-gradient(135deg,#cfd9e2,#7f96ab)}
.post-date{position:absolute;left:0;top:154px;width:62px;height:49px;background:var(--navy);color:#fff;font-family:"Montserrat",sans-serif;text-align:center;line-height:1}
.post-date span{display:block;font-size:15px;font-weight:400;padding-top:6px}
.post-date strong{display:block;font-size:22px;font-weight:700}
.post h4{margin:20px 28px 0;font-family:"Montserrat",sans-serif;font-weight:700;font-size:12px;line-height:17px;color:#222}
.post p{margin:10px 28px 0;font-family:"Montserrat",sans-serif;font-size:12px;line-height:17px;color:var(--muted)}
.post .more{margin:12px 0 0 26px;width:118px;height:34px;border:2px solid var(--navy);border-radius:20px;font-family:"Montserrat",sans-serif;font-weight:700;font-size:10px;color:var(--navy);text-align:center;line-height:30px}

/* contact form */
.contact-band{position:absolute;left:0;top:2978px;width:1200px;height:464px;background:linear-gradient(180deg,#0e5282,#0b4a78)}
.field{position:absolute;border:2px solid #d9e6f0;color:#fff;font-size:13px;display:flex;align-items:center;padding-left:18px;gap:10px}
.field svg{width:14px;height:14px;fill:#fff}
.textarea{align-items:flex-start;padding-top:12px}
.submit{position:absolute;left:505px;top:3324px;width:191px;height:48px;border-radius:26px;background:#7d7d7f;color:#fff;font-weight:700;font-size:14px;text-align:center;line-height:48px;letter-spacing:.4px}

/* footer */
.foot-div{position:absolute;top:3442px;width:1px;height:200px;background:var(--line)}
.foot-title{position:absolute;font-family:"Montserrat",sans-serif;font-weight:600;font-size:17px;color:#222;padding-left:36px;border-left:3px solid var(--blue)}
.foot-link{position:absolute;font-size:13px;color:#444;white-space:nowrap}
.copyright{position:absolute;left:0;top:3729px;width:1200px;height:62px;background:var(--foot-bar);text-align:center;line-height:62px;font-size:10px;color:#333}
</style>
</head>
<body>

<header class="site-header">
  <div class="brand"><div class="brand-dot"></div><div class="brand-name">KEYSTONE<br>ALLIES</div></div>
  <nav class="main-nav">
    <a class="nav-link active" style="left:361px" href="#">ABOUT US</a>
    <a class="nav-link" style="left:480px" href="#">WHY WE ARE</a>
    <a class="nav-link" style="left:625px" href="#">OUR SERVICES</a>
    <a class="nav-link" style="left:780px" href="#">NEWS</a>
    <a class="nav-link" style="left:879px" href="#">CLIENTS</a>
  </nav>
  <div class="nav-cta">CONTACT US</div>
</header>

<section class="hero" role="img" aria-label="Hand throwing a dart at a glowing digital target on a blue technology background">
  <svg class="arrow" style="left:30px" width="22" height="36" viewBox="0 0 22 36"><path d="M18 3 L4 18 L18 33" fill="none" stroke="#c9d6e2" stroke-width="4"/></svg>
  <svg class="arrow" style="left:1150px" width="22" height="36" viewBox="0 0 22 36"><path d="M4 3 L18 18 L4 33" fill="none" stroke="#c9d6e2" stroke-width="4"/></svg>
  <h1 class="hero-title">WELCOME TO<b>KEYSTONE ALLIES</b></h1>
  <p class="hero-text">Lorem Ipsum is simply dummy text of the printing and typesetting industry. Lorem Ipsum has been</p>
  <div class="btn-solid" style="left:155px;top:358px;width:188px;height:50px">LEARN MORE</div>
</section>

<section class="about">
  <div class="about-media" role="img" aria-label="Business team meeting photo inside a circular frame"></div>
  <div class="kicker abs" style="left:552px;top:817px">WHO WE ARE</div>
  <h2 class="sec-title abs" style="left:550px;top:838px">ABOUT <b>KEYSTONE ALLIES</b></h2>
  <div class="underline" style="left:552px;top:884px"></div>
  <p class="para abs" style="left:552px;top:907px;width:500px">Lorem Ipsum is simply dummy text of the printing and typesetting industry. Lorem Ipsum has been the industry's standard dummy text ever since the 1500s, when an unknown printer took a galley.</p>
  <p class="para abs" style="left:552px;top:1015px;width:500px">scrambled it to make a type specimen book. It has survived not only five centuries, but also the leap into electronicLorem Ipsum is simply</p>
  <div class="btn-solid" style="left:549px;top:1104px;width:188px;height:54px">LEARN MORE</div>
</section>

<section class="services">
  <svg class="abs" style="left:0;top:1236px" width="1200" height="575" viewBox="0 0 1200 575">
    <polygon points="0,0 592,63 592,575 0,575" fill="#1f3550" role="img" aria-label="Staff working together in an office, tinted navy"/>
    <polygon points="592,63 1200,0 1200,575 592,575" fill="#8a8b8d" role="img" aria-label="Colleagues meeting around a laptop, tinted grey"/>
  </svg>
  <div class="service-label" style="left:140px;top:1430px;width:404px">
    <h3>STAFF <b>AUGMENTATION</b></h3><div class="bar"></div>
    <p>Lorem Ipsum is simply dummy text of the printing and type-<br>setting industry. Lorem Ipsum has been the industry's</p>
  </div>
  <div class="btn-ghost" style="left:260px;top:1570px;width:164px;height:48px;line-height:44px">LEARN MORE</div>
  <div class="service-label" style="left:676px;top:1440px;width:436px">
    <h3>OPERATION <b>SUPPORT</b></h3><div class="bar"></div>
    <p>Lorem Ipsum is simply dummy text of the printing and type-<br>setting industry. Lorem Ipsum has been</p>
  </div>
  <div class="btn-ghost" style="left:782px;top:1580px;width:175px;height:50px;line-height:46px">LEARN MORE</div>
</section>

<section class="why" role="img" aria-label="Three colleagues discussing documents at a meeting table">
  <h2 class="sec-title abs" style="left:657px;top:150px">WHY <b>WE ARE</b></h2>
  <div class="underline" style="left:658px;top:195px"></div>
  <p class="para abs" style="left:658px;top:221px;width:475px">Lorem Ipsum is simply dummy text of the printing and typesetting industry. Lorem Ipsum has been the industry's standard dummy text ever since the 1500s, when an unknown printer took a galley. scrambled it to make a type specimen book. It has</p>
  <div class="btn-solid" style="left:657px;top:350px;width:170px;height:49px">LEARN MORE</div>
</section>

<section class="blog">
  <h2 class="sec-title abs" style="left:0;top:2420px;width:1200px;text-align:center;font-size:29px">LATEST <b>BLOG POST</b></h2>
  <div class="underline" style="left:580px;top:2464px;width:40px;height:3px;background:var(--blue)"></div>

  <article class="post" style="left:124px">
    <div class="post-photo" role="img" aria-label="Two colleagues reviewing work on a screen"></div>
    <div class="post-date"><span>JUN</span><strong>06</strong></div>
    <h4>LOREM IPSUM DOLOR SIT AMET, CON-SECTETUR ADIPISCING ELIT</h4>
    <p>Lorem Ipsum is simply dummy text of the printing and typesetting industry.</p>
    <div class="more">LEARN MORE</div>
  </article>
  <article class="post" style="left:449px">
    <div class="post-photo" role="img" aria-label="Team gathered around a table in a meeting"></div>
    <div class="post-date"><span>JUN</span><strong>04</strong></div>
    <h4>LOREM IPSUM DOLOR SIT AMET, CON-SECTETUR ADIPISCING ELIT</h4>
    <p>Lorem Ipsum is simply dummy text of the printing and typesetting industry.</p>
    <div class="more">LEARN MORE</div>
  </article>
  <article class="post" style="left:773px">
    <div class="post-photo" role="img" aria-label="Group of colleagues talking in an open office"></div>
    <div class="post-date"><span>JUN</span><strong>02</strong></div>
    <h4>LOREM IPSUM DOLOR SIT AMET, CON-SECTETUR ADIPISCING ELIT</h4>
    <p>Lorem Ipsum is simply dummy text of the printing and typesetting industry.</p>
    <div class="more">LEARN MORE</div>
  </article>
</section>

<section class="contact-band">
  <h2 class="heading abs" style="left:0;top:60px;width:1200px;text-align:center;color:#fff;font-size:26px">SPEAK TO ONE OF <b>OUR PARTNERS TODAY</b></h2>
</section>
<div class="field" style="left:281px;top:3106px;width:309px;height:46px"><svg viewBox="0 0 14 14"><circle cx="7" cy="4" r="3.5"/><path d="M0 14c0-4 3-6 7-6s7 2 7 6z"/></svg>First Name</div>
<div class="field" style="left:602px;top:3106px;width:308px;height:46px"><svg viewBox="0 0 14 14"><path d="M0 2h14v10H0z"/><path d="M0 2l7 5 7-5" stroke="#0b4f7c" fill="none" stroke-width="1.4"/></svg>Email address</div>
<div class="field" style="left:281px;top:3160px;width:309px;height:46px"><svg viewBox="0 0 14 14"><circle cx="7" cy="4" r="3.5"/><path d="M0 14c0-4 3-6 7-6s7 2 7 6z"/></svg>Last Name</div>
<div class="field" style="left:602px;top:3160px;width:308px;height:46px"><svg viewBox="0 0 14 14"><path d="M2 1l3 0 1 3-2 1.5c1 2 2.5 3.5 4.5 4.5L10 8l3 1v3c-7 1-12-5-11-11z"/></svg>Phone</div>
<div class="field textarea" style="left:283px;top:3215px;width:631px;height:85px">Leave Message</div>
<div class="submit">SUBMIT MESSAGE</div>

<footer>
  <div class="abs" style="left:155px;top:3520px;width:155px;text-align:center">
    <div style="width:52px;height:52px;border-radius:50%;background:var(--navy);margin:0 auto 14px"></div>
    <div style="font-family:'Montserrat',sans-serif;font-weight:700;color:var(--navy);font-size:22px;line-height:1.1">KEYSTONE<br>ALLIES</div>
  </div>
  <div class="foot-div" style="left:365px"></div>
  <div class="foot-div" style="left:611px"></div>
  <div class="foot-div" style="left:820px"></div>

  <div class="foot-title" style="left:365px;top:3502px">NAVIGATION</div>
  <div class="foot-link" style="left:404px;top:3547px">About Us</div>
  <div class="foot-link" style="left:404px;top:3575px">Our Products</div>
  <div class="foot-link" style="left:404px;top:3603px">Benefits</div>
  <div class="foot-link" style="left:404px;top:3631px">FAQ</div>

  <div class="foot-title" style="left:611px;top:3502px">RESOURCES</div>
  <div class="foot-link" style="left:638px;top:3547px">News</div>
  <div class="foot-link" style="left:638px;top:3575px">Partnering</div>
  <div class="foot-link" style="left:638px;top:3603px">Contact Us</div>

  <div class="foot-title" style="left:820px;top:3502px">CONTACT US</div>
  <svg class="abs" style="left:850px;top:3550px" width="32" height="32" viewBox="0 0 32 32"><circle cx="16" cy="16" r="16" fill="var(--navy)"/><path d="M11 8h3l1.5 4-2 1.5c1 2.2 2.6 3.8 4.8 4.8l1.5-2 4 1.5v3c-8 1-14-5-12.8-12.8z" fill="#fff"/></svg>
  <div class="foot-link" style="left:891px;top:3547px;font-size:12px">For Enquiry</div>
  <div class="foot-link" style="left:891px;top:3563px;font-size:16px;color:#333">+123 456 7890</div>
  <svg class="abs" style="left:852px;top:3612px" width="32" height="32" viewBox="0 0 32 32"><circle cx="16" cy="16" r="16" fill="var(--navy)"/><path d="M8 11h16v11H8z" fill="#fff"/><path d="M8 11l8 6 8-6" fill="none" stroke="var(--navy)" stroke-width="1.5"/></svg>
  <div class="foot-link" style="left:892px;top:3609px;font-size:12px">Email us</div>
  <div class="foot-link" style="left:892px;top:3625px;font-size:16px;color:#333">enquiry@keystoneallies.com</div>

  <div class="copyright">Copyright © 2022 Keystone Allies &nbsp;|&nbsp; All Right Reserved</div>
</footer>

</body>
</html>
```